Bref créative
Stationery for HR Consultancy
Business card, letterhead & compliment slip
Use same font as used in my logo
Century Gothic
Professional
Rosalind Ashcombe, FMPSB
Managing Consultant
Cambridgeshire
United Kingdom
rashcombe@VelmoreCS.example
www.VelmoreCS.example
Coloured logo on business card front. open to your suggestions for other stationery.
the purple is the primary brand colour. Green is the accent colour.
the logo colour variations that are available and colour/font descriptions are attached.
i'll provide feedback to help steer the designs if needed.
Logo with text on the card reverse. I would consider a white on purple/green background (brand colours) on the reverse, as well as the coloured logo on white background.
White background on the front of card.
letterhead text positions

```html
<!DOCTYPE html>
<html lang="en">
<head>
<meta charset="utf-8">
<title>VelmoreCS Stationery</title>
<link href="https://fonts.googleapis.com/css2?family=Questrial&display=swap" rel="stylesheet">
<style>
  :root {
    --purple: #5a1a6e;
    --purple-deep: #3f0f50;
    --green: #6aa533;
    --ink: #4a4a4a;
    --paper: #ffffff;
    --backdrop: #e9ebee;
    --edge: #d6d8dc;
    --watermark: #ece6ef;
  }
  * { margin: 0; padding: 0; box-sizing: border-box; }
  html, body { width: 1200px; height: 936px; overflow: hidden; }
  body {
    background: var(--backdrop);
    font-family: "Questrial", "Century Gothic", sans-serif;
    color: var(--ink);
    position: relative;
  }
  .sheet {
    position: absolute;
    background: var(--paper);
    border: 1px solid var(--edge);
    overflow: hidden;
  }
  .brand { display: flex; align-items: center; gap: 8px; }
  .brand-dot { border-radius: 50%; background: var(--purple); flex: none; }
  .brand-name { color: var(--purple); line-height: 1; }
  .brand-lines { display: flex; flex-direction: column; }
  .tagline { color: var(--purple); line-height: 1.3; white-space: nowrap; }
  .strap { color: var(--green); line-height: 1.3; white-space: nowrap; }

  /* letterhead */
  .letterhead { left: 182px; top: 68px; width: 388px; height: 542px; }
  .letterhead .brand { position: absolute; left: 26px; top: 32px; }
  .letterhead .brand-dot { width: 22px; height: 22px; }
  .letterhead .brand-name { font-size: 22px; }
  .letterhead .tagline { font-size: 7px; }
  .letterhead .strap { font-size: 6px; }
  .contact-block {
    position: absolute; right: 40px; top: 30px;
    font-size: 6.5px; line-height: 1.55; color: var(--ink); white-space: nowrap;
  }
  .watermark {
    position: absolute; left: 0; right: 0; top: 230px;
    text-align: center; font-size: 52px; color: var(--watermark);
  }

  .footer-band { position: absolute; left: 0; right: 0; bottom: 0; height: 16px; }
  .footer-band .green {
    position: absolute; left: 0; right: 0; bottom: 0; height: 7px; background: var(--green);
  }
  .footer-band .purple {
    position: absolute; right: 0; bottom: 0; width: 48%; height: 16px;
    background: var(--purple);
    clip-path: polygon(12px 0, 100% 0, 100% 100%, 0 100%);
    color: #fff; font-size: 7px; letter-spacing: 1.5px;
    display: flex; align-items: center; justify-content: flex-end; padding-right: 12px;
  }

  /* cover sheet */
  .cover { left: 633px; top: 46px; width: 384px; height: 569px; }
  .cover .brand { position: absolute; left: 62px; top: 256px; gap: 12px; }
  .cover .brand-dot { width: 40px; height: 40px; }
  .cover .brand-name { font-size: 38px; }
  .cover .tagline { font-size: 13px; margin-top: 4px; }
  .cover .strap { font-size: 11px; }

  /* business cards */
  .card { left: 43px; width: 185px; height: 98px; border-radius: 3px; }
  .card-front { top: 663px; }
  .card-front .brand { position: absolute; left: 10px; top: 12px; gap: 5px; }
  .card-front .brand-dot { width: 12px; height: 12px; }
  .card-front .brand-name { font-size: 12px; }
  .card-front .tagline { font-size: 4.5px; }
  .card-front .contact-block { right: 10px; top: 48px; font-size: 4.5px; text-align: right; }
  .card-front .card-rule {
    position: absolute; left: 0; right: 0; bottom: 0; height: 5px; background: var(--green);
  }
  .card-back {
    top: 779px; height: 101px; border: none;
    background: linear-gradient(160deg, #6d2483, var(--purple-deep));
  }
  .card-back .brand { position: absolute; left: 0; right: 0; top: 30px; justify-content: center; gap: 6px; }
  .card-back .brand-dot { width: 14px; height: 14px; background: #fff; }
  .card-back .brand-name { color: #fff; font-size: 16px; }
  .card-back .web {
    position: absolute; left: 0; right: 0; bottom: 10px;
    text-align: center; color: #fff; font-size: 5px; letter-spacing: 1px;
  }

  /* compliment slip */
  .slip { left: 266px; top: 670px; width: 430px; height: 203px; }
  .slip .brand { position: absolute; left: 16px; top: 20px; gap: 6px; }
  .slip .brand-dot { width: 16px; height: 16px; }
  .slip .brand-name { font-size: 16px; }
  .slip .tagline { font-size: 5px; }
  .slip .note { position: absolute; left: 16px; top: 56px; font-size: 6px; color: var(--purple); letter-spacing: 0.5px; }

  /* envelope */
  .envelope { left: 739px; top: 670px; width: 427px; height: 228px; }
  .envelope .flap {
    position: absolute; left: 0; right: 0; top: 0; height: 86px;
    background: linear-gradient(180deg, #6d2483, var(--purple));
    clip-path: polygon(0 0, 100% 0, 100% 62%, 94% 100%, 6% 100%, 0 62%);
    color: #fff; font-size: 9px; letter-spacing: 2px;
    display: flex; align-items: flex-start; justify-content: center; padding-top: 30px;
  }
</style>
</head>
<body>

  <section class="sheet letterhead">
    <div class="brand">
      <span class="brand-dot"></span>
      <div class="brand-lines">
        <span class="brand-name">VelmoreCS</span>
        <span class="tagline">Workforce Advisory Partners</span>
        <span class="strap">steady support for growing teams</span>
      </div>
    </div>
    <div class="contact-block">
      Rosalind Ashcombe, FMPSB<br>
      Managing Consultant<br>
      Harlow Vale, Northmere<br>
      rashcombe@VelmoreCS.example<br>
      www.VelmoreCS.example
    </div>
    <div class="watermark" aria-hidden="true">VelmoreCS</div>
    <div class="footer-band">
      <div class="green"></div>
      <div class="purple">WWW.VELMORECS.EXAMPLE</div>
    </div>
  </section>

  <section class="sheet cover">
    <div class="brand">
      <span class="brand-dot"></span>
      <div class="brand-lines">
        <span class="brand-name">VelmoreCS</span>
        <span class="tagline">Workforce Advisory Partners</span>
        <span class="strap">steady support for growing teams</span>
      </div>
    </div>
    <div class="footer-band">
      <div class="green"></div>
      <div class="purple">WWW.VELMORECS.EXAMPLE</div>
    </div>
  </section>

  <section class="sheet card card-front">
    <div class="brand">
      <span class="brand-dot"></span>
      <div class="brand-lines">
        <span class="brand-name">VelmoreCS</span>
        <span class="tagline">Workforce Advisory Partners</span>
      </div>
    </div>
    <div class="contact-block">
      Rosalind Ashcombe, FMPSB<br>
      Managing Consultant<br>
      rashcombe@VelmoreCS.example
    </div>
    <div class="card-rule"></div>
  </section>

  <section class="sheet card card-back">
    <div class="brand">
      <span class="brand-dot"></span>
      <span class="brand-name">VelmoreCS</span>
    </div>
    <div class="web">WWW.VELMORECS.EXAMPLE</div>
  </section>

  <section class="sheet slip">
    <div class="brand">
      <span class="brand-dot"></span>
      <div class="brand-lines">
        <span class="brand-name">VelmoreCS</span>
        <span class="tagline">Workforce Advisory Partners</span>
      </div>
    </div>
    <div class="note">With Compliments</div>
  </section>

  <section class="sheet envelope">
    <div class="flap">WWW.VELMORECS.EXAMPLE</div>
  </section>

</body>
</html>
```